Create and Design Brand Guidelines for IT Company

Brindle Networks Logo and Branding Objective
Brindle Networks is upgrading its brand assets, marketing collateral and website. The company is seeking a graphic designer's expertise to develop a style guide that creates brand consistency and communicates to internal and external stakeholders how to position the Brindle Networks brand when assigned tasks relating to the brand. The brand style guide should have information about the logo and clear usage guidelines, a recommended font to use, a colour profile including HEX code, RGB, CMYK, Pantone codes, and iconography recommendations. Details about the company tone, voice and photography usage will be added by Brindle Networks.
Look and feel
Each slider illustrates characteristics of the customer's brand and the style your logo design should communicate.

```html
<!DOCTYPE html>
<html lang="en">
<head>
<meta charset="UTF-8">
<title>Brand guidelines – 02 About</title>
<link href="https://fonts.googleapis.com/css2?family=Arimo:wght@700&family=Montserrat:wght@200;300;400;500;600&display=swap" rel="stylesheet">
<style>
  :root {
    --ink: #000000;
    --muted: #777777;
    --brand-dark: #45423b;
    --brand-green: #6ab945;
    --paper: #ffffff;
  }
  * { margin: 0; padding: 0; box-sizing: border-box; }
  html, body {
    width: 1200px;
    height: 676px;
    overflow: hidden;
    background: var(--paper);
  }
  .page {
    position: relative;
    width: 1200px;
    height: 676px;
    color: var(--ink);
    font-family: "Montserrat", sans-serif;
  }
  .section-label {
    position: absolute;
    left: 37px;
    top: 25px;
    font-family: "Arimo", Arial, sans-serif;
    font-weight: 700;
  }
  .section-label .doc-title {
    font-size: 19px;
    color: var(--muted);
    line-height: 22px;
  }
  .section-label .section-title {
    font-size: 27px;
    color: var(--ink);
    line-height: 32px;
    letter-spacing: -0.3px;
  }
  .wordmark {
    position: absolute;
    left: 84px;
    top: 160px;
    font-size: 26px;
    font-weight: 600;
    color: var(--brand-dark);
    letter-spacing: 0.2px;
  }
  .tagline {
    position: absolute;
    left: 83px;
    top: 262px;
    font-size: 52px;
    line-height: 56px;
    font-weight: 200;
    text-transform: uppercase;
    letter-spacing: 0.5px;
  }
  .tagline .highlight {
    color: var(--brand-green);
    font-weight: 500;
    display: block;
  }
  .need {
    position: absolute;
    left: 654px;
    top: 76px;
    width: 400px;
  }
  .need h2 {
    font-size: 22.5px;
    font-weight: 600;
    margin-bottom: 18px;
  }
  .need h3 {
    font-size: 20.5px;
    font-weight: 600;
    line-height: 24px;
  }
  .need p {
    font-size: 16px;
    font-weight: 400;
  }
  .need .challenge p {
    line-height: 25.3px;
  }
  .need .solution {
    margin-top: 24px;
  }
  .need .solution h3 {
    margin-bottom: 3px;
  }
  .need .solution p {
    line-height: 28.1px;
  }
</style>
</head>
<body>
<main class="page">
  <header class="section-label">
    <div class="doc-title">Brand guidelines</div>
    <div class="section-title">02 About</div>
  </header>

  <div class="wordmark">Brindle Networks</div>

  <h1 class="tagline">
    <span class="highlight">IT Support</span>
    For the<br>Ambitious<br>Business
  </h1>

  <section class="need">
    <h2>How we describe the need for Huddlewire</h2>
    <div class="challenge">
      <h3>Challenge</h3>
      <p>Global pandemics, hybrid work environments,<br>cyber security, government restrictions,<br>industry compliance, unmanned facilities and<br>human resources are just a few threats that<br>business leaders are facing each day.</p>
    </div>
    <div class="solution">
      <h3>Solution</h3>
      <p>A managed service provider (MSP) is a<br>third-party company that can remotely<br>manage a customer's Information Technology<br>(IT) infrastructure and end-user systems. The<br>rise in companies using MSPs has risen<br>significantly over the Covid-19 pandemic to<br>support businesses in digital transformation,<br>managing their complex IT environment,<br>empowering employees to work anywhere and<br>on multiple devices, and cloud storage.</p>
    </div>
  </section>
</main>
</body>
</html>
```